Healthy Meal Delivery Website Needs to be updated, current, fresh and modern

Hi there,

The current website i have is super old and outdated.

I would like a beautiful modern site that has all the same content as the previous except with a a new, modern and trustworthy feel.

The current website is https://velmorplatekitchen.com/

Target Market(s)

Health Conscious Young Professionals

Industry/Entity Type

Food Service

Font styles to use
Sans Serif

Requirements
Must have
• Modern Trustworthy feel
Should not have
• Anything out dated or cheesy or scammy

```html
<!DOCTYPE html>
<html lang="en">
<head>
<meta charset="utf-8">
<title>Velmor Plate Kitchen</title>
<link rel="stylesheet" href="https://fonts.googleapis.com/css2?family=Open+Sans:ital,wght@0,400;0,600;0,700;1,400;1,600&family=Roboto:wght@500;700;900&display=swap">
<style>
:root{
  --blue:#1a8fd1;
  --blue-deep:#1a7fc4;
  --yellow:#eee21a;
  --ink:#333a40;
  --muted:#666d73;
  --line:#d9dde0;
  --pale:#eef3f6;
  --white:#ffffff;
}
*{box-sizing:border-box;margin:0;padding:0}
html,body{width:1200px;height:4639px;overflow:hidden}
body{font-family:"Open Sans",Arial,sans-serif;color:var(--ink);background:var(--white);position:relative}
section,header,footer{position:relative;width:1200px;overflow:hidden}
.abs{position:absolute}
.heading{font-family:"Roboto",Arial,sans-serif;font-weight:700;color:var(--blue);text-transform:uppercase;letter-spacing:.5px}
.btn{display:inline-block;background:var(--yellow);color:#222;font-family:"Roboto",Arial,sans-serif;font-weight:700;font-size:14px;text-transform:uppercase;padding:14px 24px}
.photo{position:absolute}
p{font-size:14px;line-height:1.65;color:var(--muted)}

/* hero */
.hero{height:619px;background:linear-gradient(135deg,#2a2e35 0%,#4a3a40 40%,#7a4a52 62%,#9a8a78 80%,#c9c4b4 100%)}
.hero .photo{inset:0;background:radial-gradient(circle at 80% 30%,rgba(190,40,60,.45),transparent 45%),radial-gradient(circle at 65% 75%,rgba(230,220,200,.35),transparent 40%)}
.brand{left:99px;top:36px;display:flex;align-items:center;gap:10px;color:var(--white);font-family:"Roboto",Arial,sans-serif;font-weight:700;font-size:22px}
.brand i{width:26px;height:26px;background:var(--yellow);display:block}
.topbar{right:99px;top:14px;display:flex;align-items:center;gap:22px;color:var(--white);font-size:13px;font-weight:600}
.topbar span{display:flex;align-items:center;gap:7px}
.login{border:1.5px solid var(--white);padding:7px 12px;border-radius:3px;text-transform:uppercase;font-size:12px}
.nav{right:99px;top:66px;display:flex;gap:22px;font-family:"Roboto",Arial,sans-serif;font-weight:500;font-size:14px;color:var(--white);text-transform:uppercase;align-items:center}
.nav .on{color:var(--yellow)}
.hero h1{left:96px;top:190px;font-family:"Roboto",Arial,sans-serif;font-weight:900;font-size:56px;color:var(--white)}
.hero .lead{left:99px;top:280px;width:520px;font-style:italic;font-weight:600;font-size:19px;line-height:1.55;color:var(--white)}
.hero .ghost{left:99px;top:378px;border:1.5px solid var(--white);color:var(--white);font-family:"Roboto",Arial,sans-serif;font-weight:700;font-size:14px;padding:15px 20px;border-radius:3px}
.dots{left:566px;top:514px;display:flex;gap:6px}
.dots i{width:10px;height:10px;border-radius:50%;border:1.5px solid var(--white);display:block}
.dots i:first-child{background:var(--white)}

/* welcome */
.welcome{height:479px}
.welcome h2{left:99px;top:72px;font-size:36px;line-height:1.2}
.welcome .copy{left:99px;top:168px;width:480px}
.welcome .copy p+p{margin-top:18px}
.welcome .btn{position:absolute;left:99px;top:348px}
.video{left:634px;top:77px;width:362px;height:309px;border:6px solid var(--white);box-shadow:0 0 0 1px var(--line);background:linear-gradient(135deg,#c8b08a,#8a6a48 50%,#d9cfc0)}
.play{left:794px;top:218px}

/* why */
.why{height:470px;background:var(--pale)}
.why h2{left:0;width:1200px;text-align:center;top:68px;font-size:36px}
.card{top:149px;width:235px;height:241px;background:var(--white);border:1px solid var(--line);text-align:center;padding:30px 18px}
.card svg{display:block;margin:0 auto 18px}
.card h3{font-family:"Roboto",Arial,sans-serif;font-weight:700;font-size:16px;text-transform:uppercase;margin-bottom:14px}
.card p{font-size:13px;line-height:1.6}

/* included */
.included{height:588px}
.included .photo{left:99px;top:84px;width:495px;height:352px;border:6px solid var(--white);box-shadow:0 0 0 1px var(--line);background:linear-gradient(160deg,#e8e2d4,#f2a46a 35%,#e86a3a 55%,#f3d070 75%,#8a6a40)}
.included h2{left:653px;top:76px;font-size:36px;line-height:1.2}
.included .copy{left:653px;top:168px;width:470px}
.ticks{left:653px;top:258px;list-style:none}
.ticks li{display:flex;align-items:center;gap:12px;font-family:"Roboto",Arial,sans-serif;font-weight:500;font-size:13px;text-transform:uppercase;height:33px}
.included .btn{position:absolute;left:653px;top:440px}

/* subscribe */
.subscribe{height:325px;background:linear-gradient(90deg,#3a3e42,#595d60 50%,#8d9092)}
.subscribe .photo{inset:0;background:rgba(20,24,28,.35)}
.subscribe h2{left:0;width:1200px;text-align:center;top:68px;font-family:"Roboto",Arial,sans-serif;font-weight:700;font-size:36px;line-height:1.25;color:var(--white);text-transform:uppercase}
.signup{left:309px;top:195px;display:flex}
.signup .field{width:420px;height:55px;background:var(--white);padding:0 20px;display:flex;align-items:center;font-size:12px;color:#888;text-transform:uppercase}
.signup .btn{width:165px;height:55px;text-align:center;padding:18px 0}

/* blog */
.blog{height:668px}
.blog h2{left:0;width:1200px;text-align:center;top:82px;font-size:36px}
.feature{left:99px;top:170px;width:436px;height:396px;background:#e9f2fa}
.feature .photo{left:0;top:0;width:436px;height:220px;background:linear-gradient(135deg,#f4f1ec,#e8d6c4 50%,#9ab86a)}
.post h3{font-family:"Roboto",Arial,sans-serif;font-weight:700;font-size:19px;color:var(--ink);margin-bottom:8px}
.meta{display:flex;gap:12px;font-size:12px;color:var(--muted);margin-bottom:10px;align-items:center}
.meta span{display:flex;align-items:center;gap:5px}
.more{font-family:"Roboto",Arial,sans-serif;font-weight:700;font-size:13px;color:#c9b800;text-transform:uppercase;margin-top:10px}
.feature .post{position:absolute;left:35px;top:236px;width:370px}
.post p{font-size:13px}
.thumb{left:569px;width:167px;height:150px}
.side{left:770px;width:330px}
.blog .btn{position:absolute;left:565px;top:528px;padding:12px 20px}

/* reviews */
.reviews{height:461px;background:var(--blue-deep)}
.reviews h2{left:0;width:1200px;text-align:center;top:68px;font-family:"Roboto",Arial,sans-serif;font-weight:700;font-size:36px;color:var(--white)}
.review{top:181px;width:306px;height:206px;border:1.5px solid rgba(255,255,255,.8);text-align:center;padding:85px 24px 0;color:var(--white)}
.review p{color:var(--white);font-style:italic;font-size:13px;line-height:1.55}
.review strong{display:block;margin-top:16px;font-size:15px;font-weight:600}
.avatar{top:145px;width:88px;height:88px;border-radius:50%;border:4px solid var(--white);background:linear-gradient(160deg,#d8c0a8,#8a7262)}
.arrow{width:36px;height:36px;border-radius:50%;display:flex;align-items:center;justify-content:center}
.reviews .arrow{background:rgba(255,255,255,.9);top:290px}

/* menu */
.menu{height:464px;border-bottom:3px solid var(--blue)}
.menu h2{left:0;width:1200px;text-align:center;top:92px;font-size:36px}
.dish{top:176px;height:195px}
.menu .arrow{top:256px;border:1.5px solid #9aa0a5;background:var(--white)}

/* contact */
.contact{height:565px}
.contact h2{left:0;width:1200px;text-align:center;top:80px;font-size:36px}
.label{font-family:"Roboto",Arial,sans-serif;font-weight:500;font-size:19px;color:var(--ink)}
.input{height:34px;border:1px solid var(--line);font-size:12px;color:#888;padding:0 10px;display:flex;align-items:center}
.contact .btn{position:absolute;left:634px;top:408px;width:90px;text-align:center;padding:11px 0}
.info{left:780px;width:320px;display:flex;gap:16px;align-items:center;font-size:12px;color:var(--muted);line-height:1.5}
.info i{width:38px;height:38px;border-radius:50%;border:1px solid var(--line);display:flex;align-items:center;justify-content:center;flex:none}
.social{left:780px;top:350px;display:flex;gap:8px}
.social i{width:30px;height:30px;border-radius:50%;background:var(--blue);display:block}
.rule{left:99px;top:478px;width:1001px;height:1px;background:var(--line)}
.copyright{left:0;width:1200px;text-align:center;top:512px;font-size:12px;color:var(--muted)}
</style>
</head>
<body>

<header class="hero">
  <div class="photo" role="img" aria-label="Close-up of a bowl of oatmeal topped with raspberries and blackberries"></div>
  <div class="abs brand"><i></i>Velmor Plate Kitchen</div>
  <div class="abs topbar">
    <span><svg width="14" height="14" viewBox="0 0 24 24"><path fill="#eee21a" d="M6.6 10.8a15 15 0 006.6 6.6l2.2-2.2c.3-.3.7-.4 1-.2 1.1.4 2.3.6 3.6.6.6 0 1 .4 1 1V20c0 .6-.4 1-1 1A17 17 0 013 4c0-.6.4-1 1-1h3.5c.6 0 1 .4 1 1 0 1.3.2 2.5.6 3.6.1.3 0 .7-.2 1z"/></svg>416-555-0172</span>
    <span><svg width="14" height="12" viewBox="0 0 24 18"><rect width="24" height="18" rx="2" fill="#eee21a"/><path d="M1 2l11 8 11-8" stroke="#2a2e35" stroke-width="2" fill="none"/></svg>hello@velmorplate.com</span>
    <span class="login">&#9679; Client Login/Sign Up</span>
  </div>
  <nav class="abs nav">
    <span class="on">Home</span><span>Velmor Meal Plans</span><span>Menu</span><span>Pricing</span><span>About</span><span>Press</span><span>Contact</span>
    <svg width="15" height="15" viewBox="0 0 24 24"><circle cx="10" cy="10" r="7" stroke="#fff" stroke-width="3" fill="none"/><path d="M15 15l7 7" stroke="#fff" stroke-width="3"/></svg>
  </nav>
  <h1 class="abs">VELMOR PLATE KITCHEN</h1>
  <p class="abs lead">Velmor Plate veggie a la carte the Velmor Plate diet delivers diet meals to your door in toronto, gta and montreal</p>
  <span class="abs ghost">GET STARTED</span>
  <div class="abs dots"><i></i><i></i><i></i><i></i></div>
</header>

<section class="welcome">
  <h2 class="abs heading">Welcome to<br>Velmor Plate Kitchen</h2>
  <div class="abs copy">
    <p>Our fresh and delicious diet meals and snacks are made with only the best natural ingredients that nourish your body.</p>
    <p>Velmor Plate is the Toronto &amp; Montreal Diet Delivery program based on the Velmor Plate&trade;, healthy carbs and the right fats. We provide you with 3 fresh meals, 2 snacks and a dessert delivered to your door before 8am.</p>
  </div>
  <span class="btn">Read More</span>
  <div class="photo video" role="img" aria-label="Video still of hands preparing fresh vegetables on a cutting board"></div>
  <svg class="abs play" width="44" height="44" viewBox="0 0 44 44"><circle cx="22" cy="22" r="22" fill="#222" opacity=".85"/><path d="M17 13l14 9-14 9z" fill="#fff"/></svg>
</section>

<section class="why">
  <h2 class="abs heading">Why Choose Velmor Plate Kitchen?</h2>
  <div class="abs card" style="left:99px">
    <svg width="52" height="46" viewBox="0 0 52 46"><path d="M26 44S2 30 2 14A12 12 0 0126 8a12 12 0 0124 6c0 16-24 30-24 30z" fill="#1a8fd1"/><path d="M6 22h12l4-7 6 14 4-7h14" stroke="#fff" stroke-width="3" fill="none"/></svg>
    <h3>Healthy</h3><p>The Velmor Plate is a great way to ensure you are eating all the nutrients you need.</p>
  </div>
  <div class="abs card" style="left:356px">
    <svg width="48" height="48" viewBox="0 0 48 48"><circle cx="24" cy="24" r="23" fill="#1a8fd1"/><path d="M13 25l8 8 14-16" stroke="#fff" stroke-width="5" fill="none"/></svg>
    <h3>Choice</h3><p>You can choose your own meals from over 100 tasty entrees, desserts and snack foods.</p>
  </div>
  <div class="abs card" style="left:609px">
    <svg width="48" height="48" viewBox="0 0 48 48"><path d="M6 42C6 18 20 6 44 4c0 26-12 38-34 36z" fill="#1a8fd1"/><path d="M6 42L30 18" stroke="#fff" stroke-width="3"/></svg>
    <h3>Fresh</h3><p>All of our meals are real food, freshly prepared by our in house expert chefs.</p>
  </div>
  <div class="abs card" style="left:863px">
    <svg width="56" height="46" viewBox="0 0 56 46"><circle cx="28" cy="12" r="9" fill="#1a8fd1"/><circle cx="10" cy="16" r="6" fill="#1a8fd1"/><circle cx="46" cy="16" r="6" fill="#1a8fd1"/><path d="M14 44c0-12 6-20 14-20s14 8 14 20z" fill="#1a8fd1"/><path d="M0 40c0-8 4-14 10-14 3 0 5 1 7 3-3 3-5 7-5 11zM56 40c0-8-4-14-10-14-3 0-5 1-7 3 3 3 5 7 5 11z" fill="#1a8fd1"/></svg>
    <h3>Customized</h3><p>Your meals will be delivered fresh to your door, customized for your unique body type.</p>
  </div>
</section>

<section class="included">
  <div class="photo" role="img" aria-label="Plate of toast topped with scrambled eggs, smoked salmon and fresh herbs"></div>
  <h2 class="abs heading">What's Included in<br>the Program</h2>
  <p class="abs copy">Our fresh and delicious diet meals and snacks are made with only the best natural ingredients that nourish your body. Try our Velmor Plate&trade; delivery plan and start Velmor Plate weight loss now!</p>
  <ul class="abs ticks">
    <li><svg width="14" height="14" viewBox="0 0 14 14"><circle cx="7" cy="7" r="7" fill="#1a8fd1"/><path d="M4 7l2 2 4-4" stroke="#fff" stroke-width="1.8" fill="none"/></svg>What you get</li>
    <li><svg width="14" height="14" viewBox="0 0 14 14"><circle cx="7" cy="7" r="7" fill="#1a8fd1"/><path d="M4 7l2 2 4-4" stroke="#fff" stroke-width="1.8" fill="none"/></svg>Selection</li>
    <li><svg width="14" height="14" viewBox="0 0 14 14"><circle cx="7" cy="7" r="7" fill="#1a8fd1"/><path d="M4 7l2 2 4-4" stroke="#fff" stroke-width="1.8" fill="none"/></svg>Luxury</li>
    <li><svg width="14" height="14" viewBox="0 0 14 14"><circle cx="7" cy="7" r="7" fill="#1a8fd1"/><path d="M4 7l2 2 4-4" stroke="#fff" stroke-width="1.8" fill="none"/></svg>What is Phase 1?</li>
    <li><svg width="14" height="14" viewBox="0 0 14 14"><circle cx="7" cy="7" r="7" fill="#1a8fd1"/><path d="M4 7l2 2 4-4" stroke="#fff" stroke-width="1.8" fill="none"/></svg>What is Phase 2?</li>
  </ul>
  <span class="btn">Read More</span>
</section>

<section class="subscribe">
  <div class="photo" role="img" aria-label="Dimmed photo of a desk with a laptop, coffee and a plate of breakfast"></div>
  <h2 class="abs">Subscribe to my diet programs<br>and weekly letters</h2>
  <div class="abs signup"><div class="field">Email Address</div><span class="btn">Subscribe</span></div>
</section>

<section class="blog">
  <h2 class="abs heading">Latest Blog</h2>
  <div class="abs feature">
    <div class="photo" role="img" aria-label="Smiling woman holding a fork over a fresh salad"></div>
    <div class="post">
      <h3>Finibus Bonorum et Malorum</h3>
      <div class="meta"><span>&#128197; 28/12/2017</span><span>&#128100; Alex Reyes</span></div>
      <p>Nam libero tempore, cum soluta nobis est eligendi optio cumque nihil impedit quo minus id...</p>
      <div class="more">Read More</div>
    </div>
  </div>
  <div class="photo thumb" style="top:170px;background:linear-gradient(135deg,#e6d8c8,#b89478)" role="img" aria-label="Measuring tape around a waist"></div>
  <div class="abs side post" style="top:174px">
    <h3>At vero eos et accusamus et iui</h3>
    <div class="meta"><span>&#128197; 28/12/2017</span><span>&#128100; Alex Reyes</span></div>
    <p>Nam libero tempore, cum soluta nobis est eligendi optio cumque nihil impedit...</p>
    <div class="more">Read More</div>
  </div>
  <div class="photo thumb" style="top:340px;background:linear-gradient(135deg,#7a5a48,#c8a080 50%,#5a6a3a)" role="img" aria-label="Bowl of roasted meat and vegetables"></div>
  <div class="abs side post" style="top:344px">
    <h3>At vero eos et accusamus et iui</h3>
    <div class="meta"><span>&#128197; 28/12/2017</span><span>&#128100; Alex Reyes</span></div>
    <p>Nam libero tempore, cum soluta nobis est eligendi optio cumque nihil impedit...</p>
    <div class="more">Read More</div>
  </div>
  <span class="btn">View All</span>
</section>

<section class="reviews">
  <h2 class="abs">CUSTOMER REVIEWS</h2>
  <div class="abs arrow" style="left:30px"><svg width="12" height="12" viewBox="0 0 12 12"><path d="M8 1L3 6l5 5" stroke="#1a7fc4" stroke-width="2.4" fill="none"/></svg></div>
  <div class="abs arrow" style="left:1134px"><svg width="12" height="12" viewBox="0 0 12 12"><path d="M4 1l5 5-5 5" stroke="#1a7fc4" stroke-width="2.4" fill="none"/></svg></div>
  <div class="abs review" style="left:99px"><p>Nam libero tempore, cum soluta nobis est eligendi optio cumque nihil impedit quo minus id quod maxime placeat</p><strong>Tessa Marlow</strong></div>
  <div class="abs review" style="left:448px"><p>Nam libero tempore, cum soluta nobis est eligendi optio cumque nihil impedit quo minus id quod maxime placeat</p><strong>Nora Keating</strong></div>
  <div class="abs review" style="left:795px"><p>Nam libero tempore, cum soluta nobis est eligendi optio cumque nihil impedit quo minus id quod maxime placeat</p><strong>Owen Pratt</strong></div>
  <div class="abs avatar" style="left:208px" role="img" aria-label="Customer portrait"></div>
  <div class="abs avatar" style="left:557px" role="img" aria-label="Customer portrait"></div>
  <div class="abs avatar" style="left:904px" role="img" aria-label="Customer portrait"></div>
</section>

<section class="menu">
  <h2 class="abs heading">Select from over 100 menu items</h2>
  <div class="abs arrow" style="left:30px"><svg width="12" height="12" viewBox="0 0 12 12"><path d="M8 1L3 6l5 5" stroke="#666" stroke-width="2" fill="none"/></svg></div>
  <div class="abs arrow" style="left:1134px"><svg width="12" height="12" viewBox="0 0 12 12"><path d="M4 1l5 5-5 5" stroke="#666" stroke-width="2" fill="none"/></svg></div>
  <div class="photo dish" style="left:99px;width:244px;background:linear-gradient(135deg,#e0a060,#b8642c 50%,#f0d8a8)" role="img" aria-label="Grilled chicken skewers"></div>
  <div class="photo dish" style="left:353px;width:241px;background:linear-gradient(135deg,#eef0d8,#a8c470 50%,#f6f2e4)" role="img" aria-label="Fresh lettuce wraps"></div>
  <div class="photo dish" style="left:606px;width:241px;background:linear-gradient(135deg,#f4ece0,#c88a3c 50%,#e8c07a)" role="img" aria-label="Golden waffles"></div>
  <div class="photo dish" style="left:857px;width:241px;background:linear-gradient(135deg,#6a3a24,#b85a30 50%,#4a3020)" role="img" aria-label="Spiced meat stew"></div>
</section>

<section class="contact">
  <h2 class="abs heading">Contact Us</h2>
  <div class="abs label" style="left:99px;top:162px">Contact form</div>
  <div class="abs input" style="left:99px;top:219px;width:310px">Name</div>
  <div class="abs input" style="left:424px;top:219px;width:300px">Phone no</div>
  <div class="abs input" style="left:99px;top:266px;width:625px">Email</div>
  <div class="abs input" style="left:99px;top:312px;width:625px;height:78px;align-items:flex-start;padding-top:8px">Message</div>
  <span class="btn">Submit</span>
  <div class="abs label" style="left:780px;top:162px">Contact Information</div>
  <div class="abs info" style="top:208px"><i><svg width="14" height="18" viewBox="0 0 14 18"><path d="M7 0a7 7 0 017 7c0 5-7 11-7 11S0 12 0 7a7 7 0 017-7z" fill="#1a8fd1"/><circle cx="7" cy="7" r="2.5" fill="#fff"/></svg></i>Nam libero tempore, cum soluta nobis est eligendi optio</div>
  <div class="abs info" style="top:262px"><i><svg width="16" height="16" viewBox="0 0 24 24"><path fill="#1a8fd1" d="M6.6 10.8a15 15 0 006.6 6.6l2.2-2.2c.3-.3.7-.4 1-.2 1.1.4 2.3.6 3.6.6.6 0 1 .4 1 1V20c0 .6-.4 1-1 1A17 17 0 013 4c0-.6.4-1 1-1h3.5c.6 0 1 .4 1 1 0 1.3.2 2.5.6 3.6.1.3 0 .7-.2 1z"/></svg></i>416-555-0172</div>
  <div class="abs info" style="top:308px"><i><svg width="16" height="12" viewBox="0 0 24 18"><rect width="24" height="18" rx="2" fill="#1a8fd1"/><path d="M1 2l11 8 11-8" stroke="#fff" stroke-width="2" fill="none"/></svg></i>hello@velmorplate.com</div>
  <div class="abs label" style="left:780px;top:318px;display:none"></div>
  <div class="abs label" style="left:780px;top:355px;font-size:17px;display:none"></div>
  <div class="abs social" style="top:392px"><i></i><i></i><i></i><i></i></div>
  <div class="abs label" style="left:780px;top:358px;font-size:18px">Social Media</div>
  <div class="abs rule"></div>
  <div class="abs copyright">Copyright &copy; 2018, Velmor Plate Kitchen. All rights reserved.</div>
</section>

</body>
</html>
```